Postcard design to acquire new clients for my Property Management Company

I'm looking for a postcard design that I can send to prospective clients detailing information about my company and services.
Postcard should be eye catching and contain information from www.brightkeyrentals-example.com. I've provided a few screen shots for the most important information and my logo.
Target Market(s)
Real Estate
Industry/Entity Type
Real Estate
Font styles to use
Sans Serif
Requirements
Must have
- Must be eye catching!! this will be a direct mail piece - I'd like for the card to be read and not tossed in the trash immediately.
Design que from the logo.
A place to write / print the receipts name and address.
our physical address - 2287 Marble Lane, Lubbock, TX 79555.
Should not have
- the contact information on the business card is not accurate - please use info from website.

```html
<!DOCTYPE html>
<html lang="en">
<head>
<meta charset="utf-8">
<title>BrightKey Property Management – Postcard</title>
<link href="https://fonts.googleapis.com/css2?family=Montserrat:wght@300;400;600;700&family=Open+Sans:wght@400;600;700&display=swap" rel="stylesheet">
<style>
  :root{
    --page:#e6e6e6;
    --slate-top:#3c4556;
    --slate-mid:#55627a;
    --dusk:#8a6a55;
    --brick:#7a4a32;
    --brand-blue:#2170b3;
    --panel-blue:#1f5a97;
    --band:rgba(22,28,40,.82);
    --ink-blue:#1d5590;
    --white:#ffffff;
    --paper:#f4f5f7;
    --muted:#d7dde6;
    --rule:#9aa8ba;
  }
  *{box-sizing:border-box;margin:0;padding:0}
  html,body{width:1200px;height:1132px;overflow:hidden;background:var(--page)}
  body{position:relative;font-family:"Open Sans",Arial,sans-serif}

  .card{position:absolute;left:50px;width:1100px;height:530px;overflow:hidden;box-shadow:0 6px 18px rgba(0,0,0,.18)}
  .card--front{top:20px}
  .card--back{top:582px;background:var(--paper)}

  /* FRONT */
  .front-scene{position:absolute;inset:0;
    background:linear-gradient(180deg,var(--slate-top) 0%,var(--slate-mid) 45%,var(--dusk) 72%,var(--brick) 100%)}
  .brand{position:absolute;left:60px;top:48px;color:var(--white);font-family:"Montserrat",Arial,sans-serif}
  .brand__name{font-weight:600;font-size:104px;letter-spacing:18px;line-height:1}
  .brand__tag{font-weight:300;font-size:40px;letter-spacing:9px;margin-top:10px;line-height:1}
  .address-ribbon{position:absolute;left:0;top:220px;width:440px;height:150px;background:var(--brand-blue);
    clip-path:polygon(0 0,100% 0,78% 100%,0 100%);color:var(--white);padding:14px 0 0 58px;line-height:1.22}
  .address-ribbon b{display:block;font-size:23px;font-weight:700}
  .address-ribbon span{display:block;font-size:23px;font-weight:400}
  .contact-band{position:absolute;left:0;right:0;bottom:0;height:92px;background:var(--band);color:var(--white);
    display:flex;align-items:center;padding-left:54px}
  .contact-band__label{font-size:22px;line-height:1.2;padding-right:20px;border-right:2px solid var(--white)}
  .contact-band__lines{padding-left:20px;font-size:23px;line-height:1.35;font-weight:600}

  /* BACK */
  .services{position:absolute;left:30px;top:30px;width:560px;height:470px;background:var(--panel-blue);color:var(--white);
    display:grid;grid-template-columns:1fr 1fr;grid-template-rows:repeat(4,1fr);column-gap:20px;padding:16px 22px}
  .service{text-align:center;display:flex;flex-direction:column;align-items:center;justify-content:center}
  .service svg{width:34px;height:30px;margin-bottom:3px}
  .service h3{font-size:13px;font-weight:700;line-height:1.1}
  .service p{font-size:10.5px;line-height:1.3;color:var(--muted);max-width:240px}

  .back-scene{position:absolute;left:590px;right:0;bottom:0;height:170px;
    background:linear-gradient(180deg,rgba(244,245,247,1) 0%,#d9c3b2 60%,#b88c72 100%)}
  .back-brand{position:absolute;left:625px;top:14px;font-family:"Montserrat",Arial,sans-serif;color:var(--ink-blue)}
  .back-brand__name{font-size:22px;font-weight:600;letter-spacing:4px}
  .back-brand__tag{font-size:11px;letter-spacing:4px;font-weight:300;color:#7a8aa0}

  .plans{position:absolute;left:625px;top:66px;display:flex;gap:8px}
  .plan{width:148px;height:318px;background:var(--white);box-shadow:0 4px 10px rgba(0,0,0,.2);
    color:var(--ink-blue);text-align:center;padding:12px 6px;font-size:11px;line-height:1.3;font-weight:600}
  .plan h4{font-size:14px;font-weight:700;line-height:1.1}
  .plan small{display:block;font-size:9px;font-weight:400;color:#6a7a90}
  .plan .rate{font-size:26px;font-weight:700;line-height:1.1;margin-top:4px}
  .plan .rate-note{font-size:10px;font-weight:400;margin-bottom:5px}

  .mailing{position:absolute;left:625px;top:398px;width:460px;height:114px;background:var(--white);
    box-shadow:0 4px 10px rgba(0,0,0,.18);padding:10px 16px;color:var(--ink-blue)}
  .mailing__label{font-size:10px;font-weight:700;letter-spacing:2px;text-transform:uppercase}
  .mailing__line{border-bottom:1px solid var(--rule);height:25px}
  .mailing__return{position:absolute;right:16px;top:10px;font-size:10px;color:#6a7a90;text-align:right;line-height:1.3}
</style>
</head>
<body>

<section class="card card--front">
  <div class="front-scene" role="img" aria-label="Dusk photograph of downtown brick buildings and skyline"></div>
  <div class="brand">
    <div class="brand__name">BRIGHTKEY</div>
    <div class="brand__tag">PROPERTY MANAGEMENT</div>
  </div>
  <div class="address-ribbon">
    <b>BRIGHTKEY</b>
    <span>2287 Marble Lane</span>
    <b>PROPERTY MANAGEMENT</b>
    <span>Lubbock, TX 79555</span>
  </div>
  <div class="contact-band">
    <div class="contact-band__label">Contact<br>Our Team</div>
    <div class="contact-band__lines">
      Give us a call now: (806) 555-0142<br>
      Email us: info@brightkeyrentals-example.com
    </div>
  </div>
</section>

<section class="card card--back">
  <div class="back-scene" role="img" aria-label="Faded photograph of city buildings at dusk"></div>

  <div class="services">
    <div class="service">
      <svg viewBox="0 0 34 30"><path d="M3 15 17 3l14 12h-4v12H7V15z" fill="#fff"/></svg>
      <h3>Property Marketing</h3>
      <p>Tired of waiting for weeks on end, hoping to find a new tenant? Let us take over your marketing and find a qualified renter quickly.</p>
    </div>
    <div class="service">
      <svg viewBox="0 0 34 30"><circle cx="11" cy="9" r="5" fill="#fff"/><circle cx="24" cy="9" r="5" fill="#fff"/><path d="M2 26c0-7 4-10 9-10s9 3 9 10zM15 26c0-7 4-10 9-10s9 3 9 10z" fill="#fff"/></svg>
      <h3>Tenant Screening</h3>
      <p>We don't just find someone to rent your home, we find the best renters. We screen all applications using fair housing guidelines.</p>
    </div>
    <div class="service">
      <svg viewBox="0 0 34 30"><text x="17" y="26" text-anchor="middle" font-size="28" font-weight="700" fill="#fff" font-family="Open Sans,Arial,sans-serif">$</text></svg>
      <h3>Rent Collection</h3>
      <p>Stop guessing when you'll receive your rental earnings every month and say hello to consistent payments. We keep your tenants current.</p>
    </div>
    <div class="service">
      <svg viewBox="0 0 34 30"><rect x="6" y="4" width="18" height="7" rx="2" fill="#fff"/><rect x="14" y="10" width="4" height="18" fill="#fff"/></svg>
      <h3>Maintenance</h3>
      <p>Still scrambling to respond to repair requests every time a tenant calls? Let us coordinate repair work on your behalf.</p>
    </div>
    <div class="service">
      <svg viewBox="0 0 34 30"><circle cx="14" cy="12" r="8" fill="none" stroke="#fff" stroke-width="3.5"/><path d="M20 18l9 9" stroke="#fff" stroke-width="4"/></svg>
      <h3>Property Inspections</h3>
      <p>Inspections form an important part of our proactive management approach. We visit every home in our portfolio regularly.</p>
    </div>
    <div class="service">
      <svg viewBox="0 0 34 30"><path d="M3 3v24h28" fill="none" stroke="#fff" stroke-width="2.5"/><rect x="8" y="16" width="4" height="8" fill="#fff"/><rect x="15" y="11" width="4" height="13" fill="#fff"/><rect x="22" y="14" width="4" height="10" fill="#fff"/></svg>
      <h3>Financial Reporting</h3>
      <p>Keep a handle on your real estate performance. We generate monthly statements so you can review income and expenses at any moment.</p>
    </div>
    <div class="service">
      <svg viewBox="0 0 34 30"><path d="M17 2 5 6v9c0 7 5 11 12 13 7-2 12-6 12-13V6z" fill="#fff"/><path d="M17 5v20c5-2 9-5 9-10V8z" fill="#1f5a97"/></svg>
      <h3>Evictions</h3>
      <p>When things go wrong inside your rental home, rest easy with the experts on your side. We handle evictions and find new renters.</p>
    </div>
    <div class="service">
      <svg viewBox="0 0 34 30"><path d="M17 3v22M8 27h18M5 8h24" stroke="#fff" stroke-width="2.5" fill="none"/><path d="M1 18l4-10 4 10zM25 18l4-10 4 10z" fill="#fff"/></svg>
      <h3>Legal Guidance</h3>
      <p>Don't accidentally violate one of the many ordinances and housing laws governing your tenant relationship. Let us keep you compliant.</p>
    </div>
  </div>

  <div class="back-brand">
    <div class="back-brand__name">BRIGHTKEY</div>
    <div class="back-brand__tag">PROPERTY MANAGEMENT</div>
  </div>

  <div class="plans">
    <div class="plan">
      <h4>Lease Only</h4>
      <small>- You Just Need Tenants -</small>
      <div class="rate">9%</div>
      <div class="rate-note">of annual lease</div>
      Professional Photography<br>Marketing &amp; Advertising<br>Property Showings<br>Tenant Screening &amp; Qualifications<br>Lease Execution<br>Move In Coordination
    </div>
    <div class="plan">
      <h4>Full Service</h4>
      <small>- Our Most Popular -</small>
      <div class="rate">10%</div>
      <div class="rate-note">of monthly rent</div>
      Includes Leasing Service<br>24/7 Emergency Response<br>Move In &amp; Out Inspections<br>Professional Lease Enforcement<br>Schedule &amp; Oversee all Repairs<br>Pay all Invoices<br>Monthly &amp; Year End Statements<br>Annual Market Rent Analysis
    </div>
    <div class="plan">
      <h4>Premium</h4>
      <small>- Complete Care -</small>
      <div class="rate">12%</div>
      <div class="rate-note">of monthly rent</div>
      Includes Full Service Features<br>Professional Video Marketing<br>Home Warranty Coordination<br>Tenant Retention Program
    </div>
  </div>

  <div class="mailing" aria-label="Recipient address area">
    <div class="mailing__label">Mail To</div>
    <div class="mailing__return">BrightKey Property Management<br>2287 Marble Lane<br>Lubbock, TX 79555</div>
    <div class="mailing__line"></div>
    <div class="mailing__line"></div>
    <div class="mailing__line"></div>
  </div>
</section>

</body>
</html>
```